Bubble-Diagramm als Infografik für unseren Kunden aus der Immobilienbranche
Zielgruppe
Wir sind ein Software-Unternehmen mit Kunden aus allen Branchen. Ganz generell für unsere Homepage, konkret aber auch im Rahmen eines Kundenprojektes suchen wir ansprechende Beispiele und kreative Visualisierungen, wie Diagramme zu bestimmten Sachverhalten dargestellt werden können.
Aufgabenstellung
Wir möchten die Möglichkeiten darstellen, mit excelbasierten Diagrammtypen den gewissen „Wow-Effekt“ bei unseren Kunden hervorzurufen. Konkret geht es uns hier um die Erstellung eines Bubble-Diagramms. In einem Objektvergleich von Gewerbeimmobilien sollen drei Dimensionen (hier: Größe des Objekte, Gesamtmiete über die Laufzeit, effektive Miete je Quadratmeter) im Bubble-Diagramm dargestellt werden. Siehe hierzu Entwurf (.xls-Datei) anbei.
Eine Orientierung an unserem Firmenlayout (www.brenolux-net.de) ist ausdrücklich erwünscht. Die Grafik sollte aufgeräumt und klar wirken, ohne nüchtern zu sein, um auf der einen Seite mit der Form nicht vom Inhalt abzulenken, und sich auf der anderen Seite aber eben doch über die Form von der Konkurrenz, die nur mit Excel-Bordmitteln arbeitet, erkennbar abzuheben. Denkbar sind grundsätzlich auch Piktogramme oder vergleichbare, Inhalt transportierende Elemente im Graphik-Hintergrund oder in der Umrahmung, immer unter der Maßgabe, dass sie nicht zu verspielt daherkommen.
Technisch sind wir in der Lage, Excel-Diagramme auch „interaktiv“ zu gestalten, also nach Klick auf ein Diagrammelement ein Kontextmenü oder erweiterte Informationen einzublenden. Daher wünschen wir uns als Teil des Entwurfs, beispielhaft für eine Blase, die Darstellung so eines interaktiven Elements: eines Kontextmenüs / und oder eines Datenblatts.
Vorzugsweise soll die Grafik im Excel-Format zur Verfügung gestellt werden, das ist aber kein Must-have.

```html
<!DOCTYPE html>
<html lang="de">
<head>
<meta charset="utf-8">
<title>Objektvergleich Gewerbeimmobilien – Bubble-Diagramm</title>
<link rel="stylesheet" href="https://fonts.googleapis.com/css2?family=Nunito+Sans:wght@400&family=Roboto:wght@700&display=swap">
<style>
  :root {
    --frame: #d6d5d3;
    --paper: #ffffff;
    --ink: #1a1a1a;
    --icon: #444444;
    --rent-total: #a6a6a6;
    --rent-total-label: #4a4a4a;
    --size: #1c2540;
    --size-fill: #233152;
    --size-ring: #d8e9ff;
    --rent-effective: #48a6ff;
    --outline: #555555;
  }
  * { margin: 0; padding: 0; box-sizing: border-box; }
  html, body { width: 1166px; height: 1200px; overflow: hidden; background: var(--frame); }
  .canvas { position: relative; width: 1166px; height: 1200px; background: var(--frame); }
  .sheet { position: absolute; left: 30px; top: 30px; width: 1106px; height: 1140px; background: var(--paper); }
  .chart { position: absolute; left: 0; top: 0; width: 1166px; height: 1200px; }

  .legend { position: absolute; list-style: none; font-family: "Nunito Sans", sans-serif; color: var(--ink); }
  .legend-item { position: absolute; left: 0; display: flex; align-items: center; white-space: nowrap; }
  .legend-icon { flex: none; }
  .legend-dot { flex: none; border-radius: 50%; }
  .dot-total { background: var(--rent-total); }
  .dot-size { background: var(--size); }
  .dot-effective { background: var(--rent-effective); }

  .legend-large { left: 80px; top: 300px; }
  .legend-large .legend-item { font-size: 24.5px; }
  .legend-large .legend-icon { width: 60px; height: 50px; margin-right: 19px; }
  .legend-large .legend-dot { width: 27px; height: 27px; margin-right: 14px; }
  .legend-large .item-total { top: 0; }
  .legend-large .item-size { top: 56px; }
  .legend-large .item-effective { top: 115px; }

  .legend-small { left: 78px; top: 938px; }
  .legend-small .legend-item { font-size: 16px; }
  .legend-small .legend-icon { width: 40px; height: 34px; margin-right: 8px; }
  .legend-small .legend-dot { width: 18px; height: 18px; margin-right: 8px; }
  .legend-small .item-total { top: 0; }
  .legend-small .item-size { top: 37px; }
  .legend-small .item-effective { top: 74px; }

  .icon-line { fill: none; stroke: var(--icon); stroke-width: 2.4; stroke-linejoin: round; stroke-linecap: round; }
  .icon-text { font-family: "Nunito Sans", sans-serif; font-size: 13px; fill: var(--icon); }

  .object-frame { fill: none; stroke: var(--outline); stroke-width: 1.3; }
  .bubble-effective { fill: var(--rent-effective); }
  .bubble-total { fill: var(--rent-total); opacity: 0.62; }
  .bubble-size { fill: var(--size-fill); opacity: 0.86; stroke: var(--size-ring); stroke-width: 2.5; }
  .value { font-family: "Roboto", sans-serif; font-weight: 700; font-size: 22px; text-anchor: middle; dominant-baseline: central; }
  .value-light { fill: #ffffff; }
  .value-total { fill: var(--rent-total-label); }
</style>
</head>
<body>
<div class="canvas">
  <div class="sheet"></div>

  <svg class="chart" viewBox="0 0 1166 1200" xmlns="http://www.w3.org/2000/svg" role="img" aria-label="Objektvergleich von vier Gewerbeimmobilien: Gesamtmiete, Größe und Effektivmiete je Quadratmeter">
    <defs>
      <g id="object-a">
        <circle class="object-frame" r="127"/>
        <circle class="bubble-effective" cx="38" cy="7" r="78"/>
        <circle class="bubble-total" cx="-69" cy="51" r="34"/>
        <circle class="bubble-size" cx="-17" cy="51" r="35"/>
        <text class="value value-light" x="38" y="7">18</text>
        <text class="value value-light" x="-15" y="35">8</text>
        <text class="value value-total" x="-69" y="68">8</text>
      </g>
      <g id="object-b">
        <circle class="object-frame" r="127"/>
        <circle class="bubble-effective" cx="38" cy="3" r="84"/>
        <circle class="bubble-total" cx="-73" cy="53" r="33"/>
        <circle class="bubble-size" cx="-19" cy="46" r="39"/>
        <text class="value value-light" x="43" y="7">19.6</text>
        <text class="value value-light" x="-12" y="35">7.9</text>
        <text class="value value-total" x="-75" y="68">9</text>
      </g>
      <g id="object-c">
        <circle class="object-frame" r="127"/>
        <circle class="bubble-effective" cx="25" cy="-1" r="87"/>
        <circle class="bubble-total" cx="-62" cy="49" r="37"/>
        <circle class="bubble-size" cx="6" cy="42" r="43"/>
        <text class="value value-light" x="70" y="-4">20.3</text>
        <text class="value value-light" x="9" y="33">8.5</text>
        <text class="value value-total" x="-65" y="69">10</text>
      </g>
      <g id="object-d">
        <circle class="object-frame" r="127"/>
        <circle class="bubble-effective" cx="25" cy="-6" r="93"/>
        <circle class="bubble-total" cx="-62" cy="42" r="44"/>
        <circle class="bubble-size" cx="9" cy="30" r="56"/>
        <text class="value value-light" x="76" y="-32">21.2</text>
        <text class="value value-light" x="14" y="18">10.5</text>
        <text class="value value-total" x="-63" y="69">13</text>
      </g>
    </defs>

    <g class="grid-large">
      <use href="#object-a" x="648" y="269"/>
      <use href="#object-b" x="940" y="269"/>
      <use href="#object-c" x="648" y="545"/>
      <use href="#object-d" x="940" y="545"/>
    </g>

    <g class="row-small">
      <use href="#object-a" transform="translate(440 993) scale(0.635)"/>
      <use href="#object-b" transform="translate(625 993) scale(0.635)"/>
      <use href="#object-c" transform="translate(811 993) scale(0.635)"/>
      <use href="#object-d" transform="translate(997 993) scale(0.635)"/>
    </g>
  </svg>

  <svg width="0" height="0" style="position:absolute">
    <defs>
      <g id="icon-house-tag">
        <path class="icon-line" d="M4 24 L30 3 L56 24"/>
        <path class="icon-line" d="M11 19 V47 H49 V19"/>
        <path class="icon-line" d="M23 20 L30 13 L37 20 V40 H23 Z"/>
        <text class="icon-text" x="30" y="35" text-anchor="middle">€</text>
      </g>
      <g id="icon-hand-house">
        <path class="icon-line" d="M2 32 H12 V48 H2 Z"/>
        <path class="icon-line" d="M12 36 C20 33 28 34 34 37 H42 M12 45 C24 50 36 48 56 37 C53 34 49 34 44 37"/>
        <path class="icon-line" d="M28 15 L42 4 L56 15 V30 H28 Z"/>
        <circle class="icon-line" cx="42" cy="19" r="7"/>
        <text class="icon-text" x="42" y="23.5" text-anchor="middle" style="font-size:11px">€</text>
      </g>
      <g id="icon-house-size">
        <path class="icon-line" d="M3 2 V46 M9 49 H57"/>
        <path class="icon-line" d="M10 20 L32 4 L54 20"/>
        <path class="icon-line" d="M15 17 V44 H49 V17"/>
        <path class="icon-line" d="M20 27 H28 V34 H20 Z M35 44 V30 H43 V44"/>
      </g>
    </defs>
  </svg>

  <ul class="legend legend-large">
    <li class="legend-item item-total">
      <svg class="legend-icon" viewBox="0 0 60 50" aria-hidden="true"><use href="#icon-house-tag"/></svg>
      <span class="legend-dot dot-total"></span>Gesamtmiete / Mio Euro
    </li>
    <li class="legend-item item-size">
      <svg class="legend-icon" viewBox="0 0 60 50" aria-hidden="true"><use href="#icon-hand-house"/></svg>
      <span class="legend-dot dot-size"></span>Größe / m² (x1000)
    </li>
    <li class="legend-item item-effective">
      <svg class="legend-icon" viewBox="0 0 60 50" aria-hidden="true"><use href="#icon-house-size"/></svg>
      <span class="legend-dot dot-effective"></span>Effektivmiete /m² (Euro)
    </li>
  </ul>

  <ul class="legend legend-small">
    <li class="legend-item item-total">
      <svg class="legend-icon" viewBox="0 0 60 50" aria-hidden="true"><use href="#icon-house-tag"/></svg>
      <span class="legend-dot dot-total"></span>Gesamtmiete / Mio Euro
    </li>
    <li class="legend-item item-size">
      <svg class="legend-icon" viewBox="0 0 60 50" aria-hidden="true"><use href="#icon-hand-house"/></svg>
      <span class="legend-dot dot-size"></span>Größe / m² (x1000)
    </li>
    <li class="legend-item item-effective">
      <svg class="legend-icon" viewBox="0 0 60 50" aria-hidden="true"><use href="#icon-house-size"/></svg>
      <span class="legend-dot dot-effective"></span>Effektivmiete /m² (Euro)
    </li>
  </ul>
</div>
</body>
</html>
```